Velmora Outcomes Brochure Design Project

- Who we are?
Velmora Outcomes is New Internet Marketing Company Based in China.

It is our aim to provide Chinese clients with the means to internationally market their product, via the Internet.

Our primary products are Outsourced Design ( Thanks to Pixel hive and the amazing designers who use it), SEO and Virtual Hosting.

- Project Brief
Design a vibrant and fresh brochure that introduces the fundamentals of SEO. There is no restriction to the number of pages, however all the info I have included in this brief must be included.

- Colour Palette
Please see link or download the Adobe Swatch Exchange File or follow the link below
http://tintaro.example.com/#themes/search?term=5830716
Updates

Logo updated - grey background removed

Various file formats added for logo and brochure content

Brochure zip file add containing logo in different formats.

Adobe color scheme file added

The general corporate colors are:

Base Color: CMYK :0, 60, 80, 0  Hex: FF6633
Dark Orange: CMYK: 0, 72, 96, 30 Hex: B23308
Light Orange: CMYK 0, 42, 56, 0 Hex: FF9571
Grey: CMYK 0, 0, 0, 48 Hex: 858585
Light Grey: CMYK 0, 0, 0, 26 Hex: BDBDBD

Please note that I'm happy for other colors to be included, however I would like these the corporate branding colors to be clearly present through the brochure.

Hi All

First place payment has increased to $600 - Looking to see some creative designs!

Hi All

Project Deadline Extended
Reason: I have increase the budget and extend the deadline as I need to see more design.

I have attached a zip file that contains example brochures I like.

We are not keen on the table data its a little plain. We have create an info-graphic to replace one of the table and would like to see it included in the design.

Project Deadline Extended
Reason: A few designers have asked for this extension and I would like to see additional designs. Thanks Marek

Target Market(s)

- Our Target Audience is..
It is small to medium businesses looking to reach out to the international market.
Our clients still very much operate on a face to face level in business and are new to the concept of Internet marketing

However this must look professional, Marketable and Clean, with the power of connecting people globally, through SEO and design to be reflected visually in the brochure.

Industry/Entity Type

Internet

Requirements
Must have
• One or more of the FACTS that I have highlighted need to stand out on each page. These FACTS can be found the document attached to this brief and are under the section titled 'Did You Know!'. Not every fact in this section needs to be highlighted in the brochure, but each page needs to have at least, one or more fact that stands out, soemwhere on the page.
See attached document, under the heading 'Did you Know!' and use one or two of these facts to spruce up the pages!

One image/ per page or per two pages MUST be included!

- Provide stock photos and please send us a message with the additional cost of these with your submission

The Table data, that I have included in the attachment must be included in the body of the pages - BUT the table format is not necessary and you can place the information in the body like plain text.

The brochure size should be a little larger than A4.

Please design the back page, like a pocket to hold paper and other material in it that I include with this brochure.

```html
<!DOCTYPE html>
<html lang="en">
<head>
<meta charset="utf-8">
<title>Velmora Outcomes – SEO Brochure Spread</title>
<link rel="stylesheet" href="https://fonts.googleapis.com/css2?family=Yanone+Kaffeesatz:wght@300;400;700&family=Open+Sans:wght@400;700&display=swap">
<style>
:root{
  --orange:#f26430;
  --orange-text:#e8541e;
  --teal:#137290;
  --page-left:#e2e2e2;
  --page-right:#e6e6e6;
  --cell-grey:#d2d2d2;
  --white:#ffffff;
  --ink:#111111;
  --fold:#9a9a9a;
}
*{box-sizing:border-box;margin:0;padding:0}
html,body{width:1200px;height:844px;overflow:hidden;background:var(--white)}
.canvas{position:relative;width:1200px;height:844px}
.page{position:absolute;top:38px;height:744px;overflow:hidden}
.page--left{left:80px;width:517px;background:var(--page-left)}
.page--right{left:597px;width:515px;background:var(--page-right);border-left:1px solid var(--fold)}

.column-orange{position:absolute;left:48px;top:302px;width:220px;height:442px;background:var(--orange);color:var(--white);padding:16px 22px 0 4px}
.column-teal{position:absolute;left:255px;top:14px;width:238px;height:456px;background:var(--teal);color:var(--white);padding:8px 6px 0 18px}
.heading{font-family:"Yanone Kaffeesatz",sans-serif;font-weight:700;font-size:40px;line-height:1;color:var(--white)}
.subheading{font-family:"Yanone Kaffeesatz",sans-serif;font-weight:700;font-size:21px;line-height:1.05;margin:6px 0 8px}
.subheading--small{font-size:15px;margin:8px 0 2px}
.body-copy{font-family:"Yanone Kaffeesatz",sans-serif;font-weight:400;font-size:13px;line-height:15.2px}
.column-orange .heading{margin-bottom:8px}

.photo-ring{position:absolute}
.photo-ring--top{left:10px;top:48px}
.photo-ring--bottom{left:240px;top:458px}

.compare{position:absolute;left:55px;top:47px;border-collapse:collapse;table-layout:fixed;font-family:"Open Sans",sans-serif;font-size:8px;line-height:1.38}
.compare td,.compare th{vertical-align:top;padding:6px 5px;border-bottom:1px solid var(--white)}
.compare th{font-family:"Yanone Kaffeesatz",sans-serif;font-weight:700;font-size:15px;padding:1px 0;text-align:center;height:18px}
.compare .head-online{background:var(--white);color:var(--orange-text)}
.compare .head-trad{background:var(--cell-grey);color:var(--ink)}
.compare .label{background:var(--teal);color:var(--white);padding-left:8px}
.compare .online{background:var(--white);color:var(--orange-text)}
.compare .trad{background:var(--cell-grey);color:var(--ink)}
.compare p+p{margin-top:8px}
</style>
</head>
<body>
<div class="canvas">

  <section class="page page--left">
    <div class="column-teal">
      <h1 class="heading">SEO</h1>
      <h2 class="subheading">To understand SEO you have to understand search engines.</h2>
      <p class="body-copy">Search engines visit more than 40 billion pages a day and add them to their databases of pages. During this process it gives each page a page rank. This rank is based on a very complex equation containing many factors. They also create lists of ‘keywords’ that it associates to the website and it gathers other information ie link to other sites, amount of time a user spends on a page and much more.When a user searches fora word, search engines use all of this data to calculate the order it displays the results. However this is not the end of it search engines also change the results based on how popular a page or site is, so the more popular you are the more the visits you get.<br>SEO is about understanding this process and ensuring that you site is popular and ticks the right boxes. So let the experts at Velmora Outcomes get your website to the front page - all you have to do is sit back and enjoy the rewards.</p>
    </div>

    <div class="column-orange">
      <h2 class="heading">SEO</h2>
      <p class="body-copy">Velmora Outcomes doesn’t believe that traditional marketing is finished and out of the fight, but it does believe that Traditional Marketing without SEO is. However imagine hiring a sales man who works 24 hours a day, 7 days a week, who can deal with hundreds and thousands of customers at the same time and still personalize the response to consumer. Sounds amazing, right? That’s not all - he wants to work for very little money. Who is this sales man?<br>The Sales man is actually all of the international search engines. Search engines deal with over 120 billion plus searches every month.</p>
      <h3 class="subheading subheading--small">How do I Turn a Search engine into my personal sales man?</h3>
      <p class="body-copy">People trust search engines so if the search engine suggests say this sit is the best people trust it and visit the site. So how do I get a search engine to suggest mysite?</p>
    </div>

    <svg class="photo-ring photo-ring--top" width="250" height="250" viewBox="0 0 250 250">
      <defs>
        <radialGradient id="chalkboard" cx="50%" cy="45%" r="60%">
          <stop offset="0" stop-color="#3a8ea6"/>
          <stop offset="1" stop-color="#134a5c"/>
        </radialGradient>
      </defs>
      <circle cx="125" cy="125" r="114" fill="url(#chalkboard)" role="img" aria-label="Photo of a chalkboard with SEO and related words like keywords, ranking and search"/>
      <circle cx="125" cy="125" r="116" fill="none" stroke="var(--orange)" stroke-width="14"/>
    </svg>

    <svg class="photo-ring photo-ring--bottom" width="280" height="304" viewBox="0 0 280 304">
      <defs>
        <radialGradient id="searchbar" cx="55%" cy="50%" r="60%">
          <stop offset="0" stop-color="#f4f6f7"/>
          <stop offset="1" stop-color="#b9c4c9"/>
        </radialGradient>
      </defs>
      <circle cx="140" cy="140" r="124" fill="url(#searchbar)" role="img" aria-label="Photo of a magnifying glass over a browser search field"/>
      <circle cx="140" cy="140" r="126" fill="none" stroke="var(--teal)" stroke-width="14"/>
      <rect x="128" y="260" width="14" height="44" fill="var(--teal)"/>
    </svg>
  </section>

  <section class="page page--right">
    <table class="compare">
      <colgroup><col style="width:74px"><col style="width:64px"><col style="width:98px"><col style="width:62px"><col style="width:100px"></colgroup>
      <tr><td style="padding:0;border:0"></td><th colspan="2" class="head-online">Online Marketing and SEO</th><th colspan="2" class="head-trad">Traditional</th></tr>
      <tr style="height:85px"><td class="label">Cost</td><td class="online">Low Cost</td><td class="online">SEO cost are lower than traditional marketing cost and reach an international audience</td><td class="trad">High Cost</td><td class="trad"><p>Human Resources cost a lot of money.</p><p>Media coverage costs a lot of money</p></td></tr>
      <tr style="height:115px"><td class="label" style="padding-top:16px">Return On Investment</td><td class="online" style="padding-top:16px">Low Risk/High Return</td><td class="online" style="padding-top:16px">Due to its low implementation costs, SEO has a very high return on investment (ROI). This reduces the risk you need to take to maintain or increase profits</td><td class="trad" style="padding-top:16px">High Risk /Low To Medium Return</td><td class="trad" style="padding-top:16px">Traditional marketing involves high up-front costs that may never return your original investment.</td></tr>
      <tr style="height:75px"><td class="label">Availability to Business</td><td class="online">Any size business</td><td class="online">Due to low cost and high return SEO is available to any business</td><td class="trad">Medium to large corporations</td><td class="trad">Due to media costs it is virtual impossible to get wide national coverage for a small company</td></tr>
      <tr style="height:168px"><td class="label">Time required</td><td class="online">Low</td><td class="online">Imagine your business running 24 hours day. With SEO, potential customers can visit you website from anywhere at any time. They can even purchase goods whilst you’re asleep. With online marketing we can personalize automated emails to entice more purchases</td><td class="trad">High</td><td class="trad">Direct marketing requires a physical person to be interacting with the customer and even the best sales man can’t do this 24 hours a day</td></tr>
      <tr style="height:97px"><td class="label">Ability to target audience</td><td class="online">Easy</td><td class="online">By its very nature, SEO only targets those that are interested in your field or product - the bonus is that your audience is from all over the world</td><td class="trad">Difficult and costly</td><td class="trad">Traditional media is limited to either a small target audience or a wide non-targeted audience. Internet marketing allows both.</td></tr>
      <tr style="height:107px"><td class="label">Change marketing based on feedback</td><td class="online">Very Simple</td><td class="online">Internet marketing is all about helping you tailoring and automating what the consumer sees, based on feedback, to increase your return on investment</td><td class="trad"></td><td class="trad">Traditional marketing takes time to update and distribute, even in the best case scenario you have to update your brochure and get it printed.</td></tr>
    </table>
  </section>

</div>
</body>
</html>
```